Brochure about Gun Trusts

Cover Page: Image of a firearm collection or a lockbox with the title]
Headline: Protect Your Firearms Collection with a Gun Trust
Subheading: Ensure Your Legacy Remains Private and Your Wishes Are Respected
[Page 1: What is a Gun Trust?]
Definition: A legally recognized trust that allows you to collect, own, and transfer firearms, including those restricted by the NFA.
Quote: "A gun trust is a revocable trust created to hold ownership of a firearm..." - KMW
[Page 2: Benefits of a Gun Trust]
Avoid Probate: Keep your firearms out of the public probate process, maintaining your privacy.
Multi-Generational Ownership: Easily transfer ownership to beneficiaries without the need for a court proceeding.
Shared Responsibility: Allow others to legally possess and use the firearms held in the trust.
[Page 3: The Risks of Not Having a Gun Trust]
Inheritance Issues: Firearms may not be transferred as intended, potentially leading to legal complications.
Probate and Public Disclosure: Your firearms collection becomes a public record.
[Page 4: How to Set Up a Gun Trust]
Consult with an Attorney: A firearms trust attorney will create a trust that complies with all federal and state laws.
Assign a Trustee: Choose a trustee to manage the trust if you become incapacitated or pass away.
Transfer Ownership: Assign your firearms to the trust.
[Back Cover: Call to Action]
Headline: Protect Your Firearms Legacy
Contact Information: Address, Phone Number, Email, Website
Offer: Free Consultation to discuss your options

```html
<!DOCTYPE html>
<html lang="en">
<head>
<meta charset="utf-8">
<title>Gun Trust Brochure</title>
<link href="https://fonts.googleapis.com/css2?family=Montserrat:wght@300;400;500;700;800&display=swap" rel="stylesheet">
<style>
  :root{
    --bg:#efefef;
    --navy-deep:#0c2a63;
    --navy:#123b86;
    --navy-mid:#1b4a9a;
    --steel:#2f5f8f;
    --white:#ffffff;
    --silver-light:#f4f4f6;
    --silver-dark:#b9bcc4;
    --quote-ink:#143d86;
  }
  *{box-sizing:border-box;margin:0;padding:0}
  html,body{width:1200px;height:900px;overflow:hidden;background:var(--bg);font-family:'Montserrat',sans-serif;color:var(--white)}
  .stage{position:relative;width:1200px;height:900px}
  .page{position:absolute;top:215px;width:340px;height:470px;overflow:hidden;box-shadow:0 8px 24px rgba(0,0,0,.18)}

  /* Cover */
  .cover{left:60px;background:var(--navy-deep)}
  .cover-photo{position:absolute;inset:0 0 150px 0;background:
     radial-gradient(circle at 55% 52%,#3aa7d6 0,#1d5f8c 18%,transparent 38%),
     linear-gradient(160deg,#6f95b4 0%,#2f5f8f 35%,#163d6c 70%,#0c2a63 100%)}
  .cover-band{position:absolute;left:0;right:0;bottom:0;height:230px}
  .cover-text{position:absolute;left:0;right:0;bottom:34px;text-align:center;padding:0 24px}
  .cover-title{font-size:21px;line-height:1.18;letter-spacing:.5px;text-transform:uppercase}
  .cover-title b{font-weight:800}
  .cover-title span{font-weight:300}
  .rule{display:block;width:34px;height:2px;background:var(--white);margin:12px auto}
  .cover-sub{font-size:9px;font-weight:400;letter-spacing:.6px;line-height:1.5;text-transform:uppercase}

  /* Spread */
  .spread-left{left:440px;background:linear-gradient(160deg,var(--navy-mid) 0%,var(--navy) 45%,var(--navy-deep) 100%)}
  .spread-right{left:780px;background:linear-gradient(200deg,var(--navy-mid) 0%,var(--navy) 45%,var(--navy-deep) 100%)}
  .texture{position:absolute;inset:0;background:
     radial-gradient(ellipse at 70% 20%,rgba(120,170,230,.18),transparent 60%),
     radial-gradient(ellipse at 20% 90%,rgba(0,10,40,.35),transparent 60%)}
  .spread-left::after{content:"";position:absolute;top:0;right:0;width:30px;height:100%;background:linear-gradient(90deg,transparent,rgba(0,0,0,.25))}
  .spread-right::after{content:"";position:absolute;top:0;left:0;width:30px;height:100%;background:linear-gradient(270deg,transparent,rgba(0,0,0,.25))}

  .section-head{font-size:17px;line-height:1.2;text-transform:uppercase;letter-spacing:.4px}
  .section-head span{font-weight:300}
  .section-head b{font-weight:800}
  .section-head .rule{margin:8px 0 0}
  .intro{position:absolute;left:28px;top:30px;right:28px}
  .intro p{font-size:10px;line-height:1.55;margin-top:14px;font-weight:400}

  .quote{position:absolute;left:30px;top:170px;width:280px;height:280px}
  .quote-text{position:absolute;left:50px;top:72px;width:180px;text-align:center;color:var(--quote-ink);font-weight:800;font-size:16px;line-height:1.2;text-transform:uppercase}
  .quote-source{display:block;text-align:right;margin-top:6px;color:var(--navy-deep)}

  .benefits-head{position:absolute;left:28px;top:30px}
  .benefits{position:absolute;right:22px;top:95px;width:210px;list-style:none}
  .benefit{text-align:center;margin-bottom:26px}
  .benefit svg{display:block;margin:0 auto 6px}
  .benefit h3{font-size:11px;font-weight:800;text-transform:uppercase;letter-spacing:.3px;line-height:1.2}
  .benefit p{font-size:9px;line-height:1.5;margin-top:4px;font-weight:400}
</style>
</head>
<body>
<main class="stage">

  <section class="page cover">
    <div class="cover-photo" role="img" aria-label="Photo of a high-security safe with a glowing blue fingerprint scanner"></div>
    <svg class="cover-band" viewBox="0 0 340 230" preserveAspectRatio="none" aria-hidden="true">
      <defs>
        <linearGradient id="band" x1="0" y1="0" x2="0" y2="1">
          <stop offset="0" stop-color="#123b86" stop-opacity=".0"/>
          <stop offset=".35" stop-color="#123b86" stop-opacity=".85"/>
          <stop offset="1" stop-color="#0c2a63"/>
        </linearGradient>
      </defs>
      <rect width="340" height="230" fill="url(#band)"/>
      <polygon points="0,150 340,95 340,230 0,230" fill="#1b4a9a" opacity=".55"/>
    </svg>
    <div class="cover-text">
      <h1 class="cover-title"><b>Protect</b> <span>Your</span><br><b>Firearms</b> <span>Collection</span><br><span>With a</span> <b>Gun Trust</b></h1>
      <span class="rule"></span>
      <p class="cover-sub">Ensure your legacy remains private<br>and your wishes are respected</p>
    </div>
  </section>

  <section class="page spread-left">
    <div class="texture" role="img" aria-label="Faint blue circuit-board texture"></div>
    <div class="intro">
      <h2 class="section-head"><span>What is a</span><br><b>Gun Trust?</b><span class="rule"></span></h2>
      <p>A legally recognized trust that allows you to collect, own, and transfer firearms, including those restricted by the NFA.</p>
    </div>
    <div class="quote">
      <svg width="280" height="280" viewBox="0 0 280 280" aria-hidden="true">
        <defs>
          <linearGradient id="silver" x1="0" y1="0" x2="1" y2="1">
            <stop offset="0" stop-color="#f4f4f6"/>
            <stop offset=".55" stop-color="#e3e4e8"/>
            <stop offset=".62" stop-color="#c9ccd3"/>
            <stop offset="1" stop-color="#b9bcc4"/>
          </linearGradient>
        </defs>
        <circle cx="140" cy="140" r="128" fill="none" stroke="#ffffff" stroke-width="4"/>
        <circle cx="140" cy="140" r="112" fill="url(#silver)"/>
        <rect x="0" y="70" width="40" height="60" fill="#123b86"/>
        <rect x="240" y="160" width="40" height="60" fill="#123b86"/>
        <text x="6" y="132" font-family="Montserrat, sans-serif" font-weight="800" font-size="64" fill="#ffffff">“</text>
        <text x="236" y="222" font-family="Montserrat, sans-serif" font-weight="800" font-size="64" fill="#ffffff">”</text>
      </svg>
      <blockquote class="quote-text">A gun trust is a revocable trust created to hold ownership of a firearm<cite class="quote-source">- KMW</cite></blockquote>
    </div>
  </section>

  <section class="page spread-right">
    <div class="texture" role="img" aria-label="Faint blue circuit-board texture"></div>
    <h2 class="section-head benefits-head"><b>Benefits</b> <span>of</span><br><span>a</span> <b>Gun Trust</b><span class="rule"></span></h2>
    <ul class="benefits">
      <li class="benefit">
        <svg width="34" height="34" viewBox="0 0 34 34" aria-hidden="true"><circle cx="17" cy="17" r="16" fill="#fff"/><path d="M9 17 L17 10 L25 17 M11 16 V24 H23 V16" fill="none" stroke="#123b86" stroke-width="1.6"/><path d="M14 20 H20" stroke="#123b86" stroke-width="1.4"/></svg>
        <h3>Avoid Probate</h3>
        <p>Keep your firearms out of the public probate process, maintaining your privacy.</p>
      </li>
      <li class="benefit">
        <svg width="34" height="34" viewBox="0 0 34 34" aria-hidden="true"><circle cx="17" cy="17" r="16" fill="#fff"/><circle cx="12" cy="14" r="3.5" fill="none" stroke="#123b86" stroke-width="1.6"/><path d="M15.5 14 H25 M22 14 V17 M25 14 V17" stroke="#123b86" stroke-width="1.6" fill="none"/><path d="M8 23 H20 L25 20" stroke="#123b86" stroke-width="1.6" fill="none"/></svg>
        <h3>Multi-Generational<br>Ownership</h3>
        <p>Easily transfer ownership to beneficiaries without the need for a court proceeding.</p>
      </li>
      <li class="benefit">
        <svg width="34" height="34" viewBox="0 0 34 34" aria-hidden="true"><circle cx="17" cy="17" r="16" fill="#fff"/><circle cx="17" cy="12" r="3.5" fill="#123b86"/><path d="M11 20 Q17 14 23 20 Z" fill="#123b86"/><path d="M8 21 Q17 28 26 21" stroke="#123b86" stroke-width="1.6" fill="none"/></svg>
        <h3>Shared Responsibility</h3>
        <p>Allow others to legally possess and use the firearms held in the trust.</p>
      </li>
    </ul>
  </section>

</main>
</body>
</html>
```